Web Design job - Condo Debts Collection Business needs a Web Design

I need a site for a client, who works with condo debts collection, and ensure all revenues provided by condo fees will be always available to the building manager of condo on a specific date, regardless of defaults.
I have the visual identity (logo, slogan and colors) of the company, and some requirements on layout (kind of slider, menu options, phone number on a noble position, etc) - maybe I can do a sketch, but I like the idea of give some freedom to designer.

*** PLEASE, we have no interest in templates. We want something new***

Target Market(s)

I have two targets for this design: - Condominium's building manager. This target is looking for a solution to overdue debts on it's condo. - Residents on condominiums. This target wants to live in a better place, where their neighbors pay their condominium fees on time.

Number of Pages Required

1 page

Requirements
Must have
• - Slider with title, some short text related, a nice image (I prefer happy and/or peaceful family, people doing business, happy friends, and so on).
• - I have a special attention to menu. I'm looking for one I can have a nice effect, more elegant, charming, kind of innovative.
• - Phone number on the top (or clearly visible).
• - Member log in area or icon on the top (or clearly visible).
• - News/articles area.
• - Modern fonts, with good quality, sans-serif on areas where reading is more intensive (prefer Google web-fonts).
• - Colors specified on attached files.
Nice to have
• - Clear background color, cause it's better to read larger texts (like articles). Dark backgrounds makes reading difficult.
• - A site with effects (like shadows, lines, curves, gradients, lights) is usually pretty.
• - I pay attention on beautiful footers.
Should not have
• - Images with a lot of money (I don't sell richness, I sell tranquility, peace, harmony, safety).
• - Poor menu.

```html
<!DOCTYPE html>
<html lang="en">
<head>
<meta charset="utf-8">
<title>Velora — Condominium Debt Collection</title>
<link href="https://fonts.googleapis.com/css2?family=Roboto:wght@300;400;500;700&display=swap" rel="stylesheet">
<style>
:root{
  --gold:#e8ab16;
  --gold-dark:#d69a08;
  --gold-light:#f4c542;
  --ink:#2b2b2b;
  --text:#555;
  --muted:#8a8a8a;
  --line:#e4e4e4;
  --paper:#ffffff;
  --mist:#f1f1f1;
  --hero-a:#e9e3dc;
  --hero-b:#c9b7a4;
}
*{box-sizing:border-box;margin:0;padding:0}
html,body{width:1200px;height:3228px;overflow:hidden}
body{font-family:'Roboto',Arial,sans-serif;color:var(--text);background:var(--paper);position:relative}
a{text-decoration:none;color:inherit}
.abs{position:absolute}
.btn{display:inline-block;background:var(--gold);color:#fff;font-size:15px;font-weight:500;padding:12px 30px;border-radius:2px}
.btn-white{background:#fff;color:var(--ink);font-size:13px;padding:9px 22px}

/* header */
.site-header{position:absolute;top:0;left:0;width:1200px;height:100px;background:#fff;z-index:5;box-shadow:0 2px 6px rgba(0,0,0,.05)}
.brand{position:absolute;left:134px;top:26px;display:flex;align-items:center;gap:10px}
.brand-mark{width:34px;height:34px;background:var(--gold)}
.brand-name{font-size:36px;font-weight:700;color:var(--ink);letter-spacing:1px}
.brand-tag{position:absolute;left:178px;top:68px;font-size:8px;letter-spacing:1.5px;color:var(--muted);text-transform:uppercase}
.top-phone{position:absolute;right:134px;top:10px;font-size:13px;color:var(--ink);display:flex;align-items:center;gap:6px}
.main-nav{position:absolute;left:456px;top:48px;display:flex;gap:34px;font-size:15px;color:var(--ink)}
.main-nav .active{color:var(--gold);position:relative}
.main-nav .active:after{content:"";position:absolute;left:0;right:0;bottom:-10px;height:2px;background:var(--gold)}
.login-btn{position:absolute;right:134px;top:42px;background:var(--gold);color:#fff;font-size:13px;padding:8px 18px;border-radius:2px}

/* hero */
.hero{position:absolute;top:100px;left:0;width:1200px;height:520px;background:linear-gradient(100deg,#dcd9d6 0%,var(--hero-a) 38%,var(--hero-b) 100%)}
.hero-copy{position:absolute;left:134px;top:110px;color:#fff}
.hero-copy h1{font-size:58px;font-weight:300;line-height:1.08;text-shadow:0 1px 4px rgba(0,0,0,.15)}
.hero-copy .btn{margin-top:34px}
.hero-arrows{position:absolute;left:140px;top:358px;display:flex;gap:14px}
.hero-curve{position:absolute;left:0;top:500px;width:1200px;height:130px}

/* welcome */
.welcome-photo{position:absolute;left:140px;top:680px;width:210px;height:380px;background:linear-gradient(180deg,#f0e4d2,#c9a579);border-radius:4px}
.welcome-copy{position:absolute;left:600px;top:750px;width:480px}
.eyebrow{color:var(--gold);font-size:30px;font-weight:300}
.welcome-copy h2{font-size:46px;font-weight:400;color:var(--ink);margin:2px 0 18px}
.welcome-copy p{font-size:13px;line-height:1.6;margin-bottom:10px}
.welcome-copy .btn{margin-top:14px}

/* services */
.services{position:absolute;top:1060px;left:0;width:1200px;height:620px}
.services-title{position:absolute;top:140px;width:1200px;text-align:center;color:#fff}
.services-title .mark{width:30px;height:30px;background:#fff;margin:0 auto 16px}
.services-title h2{font-size:38px;font-weight:300}
.service-card{position:absolute;top:240px;width:290px;height:280px;border:2px solid rgba(255,255,255,.85);text-align:center;color:#fff;padding:30px 26px}
.service-card svg{display:block;margin:0 auto 14px}
.service-card h3{font-size:20px;font-weight:500;margin-bottom:12px}
.service-card p{font-size:12px;line-height:1.55;margin-bottom:20px}

/* news */
.news-title{position:absolute;top:1715px;width:1200px;text-align:center;font-size:40px;font-weight:300;color:var(--ink)}
.news-card{position:absolute;top:1808px;width:290px}
.news-photo{height:190px;position:relative}
.news-date{position:absolute;left:50%;bottom:-12px;transform:translateX(-50%);background:var(--gold);color:#fff;font-size:11px;padding:5px 14px}
.news-card h4{margin-top:28px;font-size:15px;font-weight:500;color:var(--ink);line-height:1.35}
.news-card p{margin-top:10px;font-size:11.5px;line-height:1.55;color:var(--muted)}
.news-card .more{display:block;margin-top:10px;font-size:11px;color:var(--gold);font-weight:500}
.dots{position:absolute;top:2180px;left:0;width:1200px;display:flex;justify-content:center;gap:10px}
.dots span{width:11px;height:11px;border-radius:50%;background:#bbb}
.dots span.on{background:#777}

/* testimonials */
.testimonials{position:absolute;top:2220px;left:0;width:1200px;height:560px}
.testimonials h2{position:absolute;top:90px;width:1200px;text-align:center;font-size:40px;font-weight:300;color:var(--ink)}
.quote{position:absolute;background:#fff;text-align:center;padding:26px 28px;box-shadow:0 2px 8px rgba(0,0,0,.06)}
.quote p{font-size:12px;line-height:1.6;color:var(--muted)}
.quote .who{margin-top:24px;font-size:15px;color:var(--ink)}
.quote .role{font-size:11px;color:var(--muted)}
.quote.featured{background:var(--gold);box-shadow:0 6px 16px rgba(0,0,0,.12)}
.quote.featured p,.quote.featured .who,.quote.featured .role{color:#fff}
.quote-mark{position:absolute;right:22px;bottom:40px;font-size:54px;font-weight:700;color:#d9d9d9;line-height:1}
.featured .quote-mark{color:rgba(255,255,255,.55)}
.avatar{position:absolute;width:60px;height:60px;border-radius:50%;background:linear-gradient(#d7c7b5,#9c8672);border:3px solid #fff}
.t-arrow{position:absolute;top:2490px}

/* footer */
.site-footer{position:absolute;top:2760px;left:0;width:1200px;height:468px;background:#fff}
.skyline{position:absolute;left:0;top:0;width:1200px;height:420px;background:linear-gradient(180deg,#fff 0%,#f3f3f3 100%)}
.footer-brand{position:absolute;left:140px;top:70px}
.footer-brand .brand-name{font-size:34px}
.socials{position:absolute;left:140px;top:160px;display:flex;gap:14px}
.socials span{width:24px;height:24px;border-radius:50%;background:#3a3a3a}
.foot-col{position:absolute;top:75px}
.foot-col h5{font-size:16px;font-weight:700;color:var(--ink);letter-spacing:.5px;margin-bottom:14px}
.foot-col li{list-style:none;font-size:12.5px;line-height:2;color:var(--text)}
.contact-row{display:flex;gap:8px;align-items:flex-start}
.copyright{position:absolute;left:0;bottom:0;width:1200px;height:48px;line-height:48px;text-align:center;font-size:11px;color:var(--muted);border-top:1px solid var(--line);background:#fff}
</style>
</head>
<body>

<header class="site-header">
  <div class="brand"><span class="brand-mark"></span><span class="brand-name">velora</span></div>
  <div class="brand-tag">Condominium Collections</div>
  <div class="top-phone">
    <svg width="13" height="13" viewBox="0 0 24 24"><path fill="#e8ab16" d="M6.6 10.8a15 15 0 0 0 6.6 6.6l2.2-2.2a1 1 0 0 1 1-.25 11.4 11.4 0 0 0 3.6.57 1 1 0 0 1 1 1V20a1 1 0 0 1-1 1A17 17 0 0 1 3 4a1 1 0 0 1 1-1h3.5a1 1 0 0 1 1 1c0 1.25.2 2.45.57 3.57a1 1 0 0 1-.25 1z"/></svg>
    (555) 014-2736
  </div>
  <nav class="main-nav">
    <a class="active">Home</a><a>About Us</a><a>Services</a><a>Why Us</a><a>Blogs</a>
  </nav>
  <a class="login-btn">Member Login</a>
</header>

<section class="hero" role="img" aria-label="Happy family with a baby relaxing together on the living room floor">
  <div class="hero-copy">
    <h1>We Work with<br>Condo Debts<br>Collection</h1>
    <a class="btn">Learn More</a>
  </div>
  <div class="hero-arrows">
    <svg width="20" height="30" viewBox="0 0 20 30"><path d="M15 3 4 15l11 12" fill="none" stroke="#fff" stroke-width="3"/></svg>
    <svg width="20" height="30" viewBox="0 0 20 30"><path d="M5 3l11 12L5 27" fill="none" stroke="#fff" stroke-width="3"/></svg>
  </div>
</section>
<svg class="hero-curve" viewBox="0 0 1200 130" preserveAspectRatio="none">
  <path d="M0 40 Q600 150 1200 40 L1200 130 L0 130Z" fill="#fff"/>
  <path d="M0 46 Q600 150 1200 46" fill="none" stroke="#e8ab16" stroke-width="3"/>
  <path d="M0 58 Q600 150 1200 58" fill="none" stroke="#f4c542" stroke-width="2"/>
</svg>

<section class="welcome">
  <div class="welcome-photo" role="img" aria-label="Cupped hands holding a cloth savings sack"></div>
  <div class="welcome-copy">
    <div class="eyebrow">Welcome</div>
    <h2>What Velora Do</h2>
    <p>We make sure every condominium receives its fee revenue on the agreed date each month, so the building manager can plan maintenance and services without worrying about late payments.</p>
    <p>Our team handles overdue accounts with care and discretion, talking with residents, arranging fair payment plans and keeping clear records that managers can follow at any time.</p>
    <a class="btn">Learn More</a>
  </div>
</section>

<section class="services">
  <svg class="abs" style="left:0;top:0" width="1200" height="620" viewBox="0 0 1200 620" preserveAspectRatio="none">
    <path d="M0 60 Q600 -20 1200 60 L1200 560 Q600 640 0 560Z" fill="#e8ab16"/>
    <path d="M0 40 Q600 -30 1200 40" fill="none" stroke="#f4c542" stroke-width="3"/>
    <path d="M0 80 Q600 0 1200 80 L1200 60 Q600 -20 0 60Z" fill="#f2bd35"/>
    <path d="M0 580 Q600 660 1200 580" fill="none" stroke="#f4c542" stroke-width="3"/>
  </svg>
  <div class="services-title"><div class="mark"></div><h2>Our Services</h2></div>

  <div class="service-card" style="left:132px">
    <svg width="40" height="40" viewBox="0 0 40 40"><rect x="6" y="4" width="24" height="30" fill="none" stroke="#fff" stroke-width="2"/><path d="M11 12h14M11 18h14M11 24h9" stroke="#fff" stroke-width="2"/><circle cx="31" cy="30" r="6" fill="#fff"/></svg>
    <h3>Debt Collection</h3>
    <p>We follow up overdue condo fees with residents, agree on fair plans and keep the budget steady.</p>
    <a class="btn btn-white">Learn More</a>
  </div>
  <div class="service-card" style="left:455px">
    <svg width="40" height="40" viewBox="0 0 40 40"><rect x="8" y="4" width="24" height="32" fill="none" stroke="#fff" stroke-width="2"/><path d="M13 20l5 5 9-10" fill="none" stroke="#fff" stroke-width="2.5"/></svg>
    <h3>Invoice Checking</h3>
    <p>Every invoice is reviewed against the building records so nothing is missed or paid twice.</p>
    <a class="btn btn-white">Learn More</a>
  </div>
  <div class="service-card" style="left:778px">
    <svg width="40" height="40" viewBox="0 0 40 40"><path d="M20 4 34 10v10c0 8-6 13-14 16C12 33 6 28 6 20V10z" fill="none" stroke="#fff" stroke-width="2"/><path d="M14 20l4 4 8-8" fill="none" stroke="#fff" stroke-width="2.5"/></svg>
    <h3>Insolvency Services</h3>
    <p>When a unit owner cannot pay, we guide the process calmly and protect the shared fund.</p>
    <a class="btn btn-white">Learn More</a>
  </div>
</section>

<h2 class="news-title">News &amp; Articles</h2>
<article class="news-card" style="left:140px">
  <div class="news-photo" role="img" aria-label="Residents chatting in a bright apartment building lobby" style="background:linear-gradient(135deg,#8fa3b5,#d6dde3)"><span class="news-date">12 May 2018</span></div>
  <h4>Clear steps to settle late condo fees without conflict</h4>
  <p>Simple habits that help managers keep neighbours on good terms while the budget stays on track.</p>
  <a class="more">READ MORE</a>
</article>
<article class="news-card" style="left:455px">
  <div class="news-photo" role="img" aria-label="Two people shaking hands over a desk with documents" style="background:linear-gradient(135deg,#6b5a48,#c8b39a)"><span class="news-date">08 May 2018</span></div>
  <h4>How a guaranteed monthly revenue changes building plans</h4>
  <p>Knowing the money arrives on time lets managers schedule repairs and upgrades with confidence.</p>
  <a class="more">READ MORE</a>
</article>
<article class="news-card" style="left:770px">
  <div class="news-photo" role="img" aria-label="Smiling family sitting together on a sofa at home" style="background:linear-gradient(135deg,#c79a7a,#efd9c4)"><span class="news-date">02 May 2018</span></div>
  <h4>Why residents enjoy living where fees are paid on time</h4>
  <p>Well kept shared spaces and calm meetings are the quiet benefits of a healthy condo fund.</p>
  <a class="more">READ MORE</a>
</article>
<div class="dots"><span></span><span class="on"></span><span></span></div>

<section class="testimonials">
  <svg class="abs" style="left:0;top:0" width="1200" height="560" viewBox="0 0 1200 560" preserveAspectRatio="none">
    <path d="M0 60 Q600 -30 1200 60 L1200 560 L0 560Z" fill="#eeeeee"/>
    <path d="M0 50 Q600 -40 1200 50" fill="none" stroke="#e8ab16" stroke-width="3"/>
  </svg>
  <h2>What Our Client Says</h2>
</section>
<svg class="t-arrow" style="left:140px" width="20" height="36" viewBox="0 0 20 36"><path d="M16 3 4 18l12 15" fill="none" stroke="#999" stroke-width="2.5"/></svg>
<svg class="t-arrow" style="left:1040px" width="20" height="36" viewBox="0 0 20 36"><path d="M4 3l12 15L4 33" fill="none" stroke="#999" stroke-width="2.5"/></svg>

<div class="quote" style="left:200px;top:2400px;width:230px;height:250px">
  <p>Since we started working together our building has received every fee on time and meetings are far calmer.</p>
  <div class="who">By Author Name</div><div class="role">Condo Manager</div>
  <span class="quote-mark">”</span>
</div>
<div class="quote featured" style="left:478px;top:2380px;width:250px;height:300px">
  <p>The team treated our residents with respect and still recovered the overdue fees. Our budget has never been this steady and the building looks better every month.</p>
  <div class="who">Marcus Hale</div><div class="role">Condo Manager</div>
  <span class="quote-mark">”</span>
</div>
<div class="quote" style="left:775px;top:2400px;width:230px;height:250px">
  <p>Clear reports, friendly contact and no more surprises at the end of the month for our board.</p>
  <div class="who">By Author Name</div><div class="role">Condo Resident</div>
  <span class="quote-mark">”</span>
</div>
<div class="avatar" role="img" aria-label="Client portrait" style="left:285px;top:2636px"></div>
<div class="avatar" role="img" aria-label="Client portrait" style="left:573px;top:2664px;width:64px;height:64px"></div>
<div class="avatar" role="img" aria-label="Client portrait" style="left:860px;top:2636px"></div>

<footer class="site-footer">
  <div class="skyline" role="img" aria-label="Faint city skyline of apartment towers"></div>
  <div class="footer-brand"><div class="brand"><span class="brand-mark"></span><span class="brand-name">velora</span></div></div>
  <div class="socials"><span></span><span></span><span></span><span></span><span></span></div>
  <div class="foot-col" style="left:480px">
    <h5>COMPANY</h5>
    <ul><li>Home</li><li>About Us</li><li>Why Us</li><li>Our Services</li></ul>
  </div>
  <div class="foot-col" style="left:660px">
    <h5>RESOURCES</h5>
    <ul><li>Testimonials</li><li>Team</li><li>News &amp; Articles</li><li>Contact Us</li></ul>
  </div>
  <div class="foot-col" style="left:860px">
    <h5>CONTACT US</h5>
    <ul>
      <li class="contact-row">☎ (555) 014-2736</li>
      <li class="contact-row">✉ hello@velora-condo.com</li>
      <li class="contact-row">⌂ 48 Linden Avenue, Suite 210<br>Riverton, 10482</li>
    </ul>
  </div>
  <div class="copyright">© 2018 Velora. All rights reserved. Terms of Use</div>
</footer>

</body>
</html>
```